Catering Company Needs a Web Page Design

I already have my logo, and so I'm moving onto the next phase.. the web page design. Zestora is a gourmet catering company based in orlando, fl, set to launch in 2015. I will have a store location to host cooking classes as well.... and will be uploading cooking demo videos to my website weekly. Id like a blog section, and about, a video section, contact form, Services, Menu Samples..... My logo and concept is modern, innovative, and fun! I am targeting middle class to upper middle class women, but i want the site to be super unique.

Industry/Entity Type

Catering

Requirements
Must have
• The front/main page must have the logo... and the quillnote registry's definition of "zestora". I like movement... maybe the top banner can move somehow.. Im not a web designer, so i wont really know until I start seeing some examples. For now I dont have photos of my own cooking, so if you could use stock photos of catering dishes.. I uploaded a transparent logo also, maybe that could be the top banner placed over a scene of expertly plated hordourves...

```html
<!DOCTYPE html>
<html lang="en">
<head>
<meta charset="utf-8">
<title>Zestora – Gourmet Catering &amp; Cooking Classes</title>
<link href="https://fonts.googleapis.com/css2?family=Open+Sans:wght@300;400;600;700&family=Lato:wght@400;700&display=swap" rel="stylesheet">
<style>
:root{
  --ink:#333333;
  --text:#555555;
  --muted:#777777;
  --orange-top:#f7a21b;
  --orange-bottom:#ef7a06;
  --green:#7cb82f;
  --green-top:#97c94a;
  --green-bottom:#5c9a1c;
  --footer:#3a3a3c;
  --line:#dcdcdc;
  --page:#ffffff;
}
*{margin:0;padding:0;box-sizing:border-box}
html,body{width:1071px;height:1200px;overflow:hidden;background:var(--page)}
body{position:relative;font-family:"Open Sans",sans-serif;color:var(--text)}
.top-strip{position:absolute;left:0;top:0;width:1071px;height:7px;background:#e8e8e8}
.brand{position:absolute;left:88px;top:28px}
.brand-name{display:flex;align-items:center;gap:8px;font-family:"Open Sans",sans-serif;font-weight:700;font-size:62px;line-height:1;color:var(--ink);letter-spacing:-1px}
.brand-dot{width:16px;height:16px;border-radius:50%;background:var(--orange-bottom)}
.brand-tagline{position:absolute;left:58px;top:68px;font-size:11.5px;color:#666;white-space:nowrap}
.order{position:absolute;right:91px;top:58px;text-align:right;font-family:"Lato",sans-serif}
.order-label{font-size:18px;color:var(--green);line-height:1.1}
.order-phone{font-size:23px;color:var(--ink);line-height:1.1}
.hero{position:absolute;left:0;top:144px;width:1071px;height:420px}
.hero svg{display:block}
.hero-copy{position:absolute;left:0;top:148px;width:1071px;text-align:center;color:#222}
.hero-title{font-family:"Open Sans",sans-serif;font-weight:700;font-size:49px;line-height:1.1}
.hero-line{font-weight:700;font-size:23px;line-height:1.35}
.nav{position:absolute;left:88px;top:123px;width:896px;height:46px;border-radius:3px;background:linear-gradient(var(--orange-top),var(--orange-bottom));display:flex;padding-left:40px}
.nav a{font-family:"Lato",sans-serif;font-size:16.5px;color:#fff;text-decoration:none;line-height:46px;padding:0 23px;border-right:1px solid rgba(255,255,255,.35)}
.nav a:last-child{border-right:none}
.welcome{position:absolute;left:88px;top:594px;width:896px;text-align:center}
.welcome h1{font-weight:300;font-size:31px;color:#444;line-height:1.2;margin-bottom:4px}
.welcome .lead{font-size:15px;color:#666;line-height:1.4}
.welcome .body{font-size:11.3px;color:#777;line-height:1.7}
.card{position:absolute;top:748px;height:299px;border:1px solid var(--line);border-radius:3px;background:#fff}
.blog{left:91px;width:282px;padding:18px 20px}
.blog h2{font-weight:400;font-size:23px;color:#222;margin-bottom:8px}
.post{margin-bottom:11px}
.post h3{font-weight:400;font-size:14px;color:#333;line-height:1.3}
.post p{font-size:10.6px;color:#888;line-height:1.6}
.more{font-size:11.5px;color:var(--green);font-weight:600;display:flex;align-items:center;gap:5px;margin-top:6px}
.video{left:383px;width:308px;padding:12px}
.video-frame{position:relative;width:284px;height:200px;border-radius:2px;overflow:hidden}
.video h2{font-weight:400;font-size:20px;color:#222;margin:8px 4px 2px}
.video p{font-size:11.3px;color:#888;line-height:1.6;margin-left:5px}
.contact{left:703px;width:281px;border:none;background:linear-gradient(var(--green-top),var(--green-bottom));padding:20px 22px 0 25px}
.contact h2{font-weight:400;font-size:20.5px;color:#fff;margin-bottom:12px}
.field{background:#fff;border-radius:2px;height:31px;margin-bottom:8px;font-size:11px;color:#888;padding:8px 13px}
.field.message{height:71px}
.submit{position:absolute;right:21px;top:249px;width:115px;height:30px;background:#2f2f2f;color:#fff;border-radius:3px;font-size:13px;text-align:center;line-height:30px}
.footer{position:absolute;left:0;top:1101px;width:1071px;height:99px;background:var(--footer)}
.footer-nav{position:absolute;left:88px;top:29px;font-size:12.8px;font-weight:600;color:#fff;white-space:nowrap}
.footer-nav span{margin:0 7px;font-weight:400}
.copyright{position:absolute;left:88px;top:56px;font-size:11px;font-weight:300;color:#ddd}
.social{position:absolute;right:95px;top:28px;display:flex;gap:4px}
.social i{display:block;width:27px;height:27px;border-radius:50%;background:#fff}
</style>
</head>
<body>
<div class="top-strip"></div>

<header>
  <div class="brand">
    <div class="brand-name">zestora<span class="brand-dot"></span></div>
    <div class="brand-tagline">Gourmet Catering &amp; Cooking Classes</div>
  </div>
  <div class="order">
    <div class="order-label">ORDER NOW</div>
    <div class="order-phone">555.204.3187</div>
  </div>
</header>

<section class="hero">
  <svg width="1071" height="420" viewBox="0 0 1071 420">
    <defs>
      <linearGradient id="heroTone" x1="0" y1="0" x2="1" y2="0">
        <stop offset="0" stop-color="#c9a07a"/>
        <stop offset=".3" stop-color="#d8744a"/>
        <stop offset=".55" stop-color="#e9e3da"/>
        <stop offset=".8" stop-color="#f2f0ec"/>
        <stop offset="1" stop-color="#7a5a44"/>
      </linearGradient>
      <linearGradient id="curveShade" x1="0" y1="0" x2="0" y2="1">
        <stop offset="0" stop-color="#d6d6d6"/>
        <stop offset="1" stop-color="#ffffff"/>
      </linearGradient>
    </defs>
    <rect role="img" aria-label="Banner photo of a catered table with plated dishes, salads and wine glasses" width="1071" height="420" fill="url(#heroTone)"/>
    <path d="M0 384 Q535 335 1071 384 L1071 420 L0 420 Z" fill="url(#curveShade)"/>
    <path d="M0 392 Q535 343 1071 392 L1071 420 L0 420 Z" fill="#fff"/>
    <path d="M488 385 Q493 380 503 378 L570 378 Q580 380 585 385 L585 411 L488 411 Z" fill="#555"/>
    <circle cx="515" cy="395" r="6.5" fill="#8cc63f"/>
    <circle cx="530" cy="395" r="6.5" fill="#fff"/>
    <circle cx="545" cy="395" r="6.5" fill="#fff"/>
    <circle cx="560" cy="395" r="6.5" fill="#fff"/>
  </svg>
  <div class="hero-copy">
    <div class="hero-title">Zestora</div>
    <div class="hero-line">Those who are overly zealous and enthusiastic about</div>
    <div class="hero-line">eating, cooking, and fine dining.</div>
  </div>
</section>

<nav class="nav">
  <a href="#">HOME</a><a href="#">ABOUT US</a><a href="#">OUR FOOD</a><a href="#">BOOK NOW</a><a href="#">VIDEO</a><a href="#">BLOG</a><a href="#">CONTACT US</a>
</nav>

<section class="welcome">
  <h1>Welcome to Zestora Mainpage..</h1>
  <p class="lead">Phasellus felis dolor scelerisque a tempus eget lobortis id libero Aliquam nec erat at purus cursus interdum Vestibulum</p>
  <p class="body">ligula augue bibendum accumsan vestibulum ut commodo a mi Morbi ornare gravida elit Integer congue augue et malesuada iaculis ipsum dui aliquet felis at cursus magna nisl nec elit Vestibulum gravida Praesent elementum elit at tellus Malesuada nec ultricies sit amet porttitor mattis enim In massa libero interdum nec interdum vel blandit sed nulla&nbsp; Nulla sit amet diam Duis non nunc libero a tempus libero lectus feugiat felis Morbi diam mauris viverra</p>
</section>

<article class="card blog">
  <h2>Recent Blog Post</h2>
  <div class="post"><h3>Etiam eu urna Sed</h3><p>Morbi diam mauris viverra in gravida eu mattis in ante Morbi eget arcu Morbi porta libero</p></div>
  <div class="post"><h3>Phasellus felis dolor</h3><p>Morbi diam mauris viverra in gravida eu mattis in ante Morbi eget arcu Morbi porta libero</p></div>
  <div class="post"><h3>Donec convallis pede venenatis</h3><p>Aliquam nec erat at purus cursus interdum Vestibulum ligula augue bibendum accumsan vestibulum ut commodo</p></div>
  <div class="more">READ MORE BLOG
    <svg width="5" height="8" viewBox="0 0 5 8"><path d="M0 0 L5 4 L0 8 Z" fill="#7cb82f"/></svg>
  </div>
</article>

<article class="card video">
  <div class="video-frame">
    <svg width="284" height="200" viewBox="0 0 284 200">
      <defs>
        <radialGradient id="dishTone" cx=".5" cy=".55" r=".7">
          <stop offset="0" stop-color="#8a4a3a"/>
          <stop offset=".55" stop-color="#c7803a"/>
          <stop offset="1" stop-color="#5c5a2a"/>
        </radialGradient>
      </defs>
      <rect role="img" aria-label="Video still of a plated beef tenderloin with roasted vegetables" width="284" height="200" fill="url(#dishTone)"/>
      <circle cx="142" cy="100" r="27" fill="#fff" fill-opacity=".88"/>
      <path d="M135 87 L154 100 L135 113 Z" fill="#222"/>
    </svg>
  </div>
  <h2>Watch Our Video</h2>
  <p>Aliquam nec erat at purus cursus interdum Vestibulum ligula augue bibendum accumsan</p>
</article>

<aside class="card contact">
  <h2>QUICK CONTACT FORM</h2>
  <div class="field">Your Name</div>
  <div class="field">Email address</div>
  <div class="field">Phone no.</div>
  <div class="field message">Message</div>
  <div class="submit">SUBMIT NOW</div>
</aside>

<footer class="footer">
  <div class="footer-nav">Home<span>|</span>ABOUT US<span>|</span>OUR FOOD<span>|</span>BOOK NOW<span>|</span>VIDEO<span>|</span>BLOG<span>|</span>CONTACT US</div>
  <div class="copyright">© 2014 Company Name&nbsp; All right reserved&nbsp; Term of Use</div>
  <div class="social"><i></i><i></i><i></i><i></i></div>
</footer>
</body>
</html>
```